Private lender of mortgages and rent to own housing

need a website that reflects real estate especially mortgage lending and rent to own houses..
Sections as follows
Home About Types of mortgages Rent to own Contact us
Target Market(s)
consumers who require non traditonal mortgages
Industry/Entity Type
Mortgage
Coding
Coded - Design and coding required
Number of Pages Required
4 page
Font styles to use
Sans Serif
Colors
Designer to choose colors to be used in the design.
Requirements
Must have
- background pictures on pages. with nice picture on homepage of houses or a community
Nice to have
- contact us form i supplied a ink to

```html
<!DOCTYPE html>
<html lang="en">
<head>
<meta charset="utf-8">
<title>Harbourline Lending Group</title>
<link href="https://fonts.googleapis.com/css2?family=Open+Sans:wght@400;600;700&family=Roboto+Condensed:wght@400&display=swap" rel="stylesheet">
<style>
:root{
  --navy:#3a3995;
  --navy-deep:#10104a;
  --ink:#222;
  --muted:#6b6b6b;
  --line:#d9d9d9;
  --footer:#262626;
  --white:#fff;
  --social:#1a8fd6;
}
*{margin:0;padding:0;box-sizing:border-box}
html,body{width:1200px;height:2903px;overflow:hidden;background:var(--white)}
body{position:relative;font-family:"Open Sans",Arial,sans-serif;color:var(--ink)}
.abs{position:absolute}
/* header */
.phone{left:91px;top:40px;font-size:23px;color:var(--ink);display:flex;align-items:center;gap:10px}
.brand{left:0;width:1200px;top:72px;text-align:center;font-size:14px;font-weight:700;color:var(--navy-deep);letter-spacing:.3px}
.brand-mark{display:inline-block;width:12px;height:12px;background:var(--navy-deep);margin-right:8px;vertical-align:-1px}
.social{right:91px;top:43px;display:flex;gap:10px}
.social span{width:22px;height:22px;border-radius:3px;background:var(--social)}
.social span:last-child{background:#dc4a38}
.nav{left:0;top:116px;width:1200px;height:54px;border:1px solid var(--line);border-bottom:none}
.nav a{position:absolute;top:0;height:54px;line-height:54px;font-size:15px;color:var(--ink);text-decoration:none;text-align:center}
.nav a.active{background:var(--navy-deep);color:var(--white)}
/* hero */
.hero{left:0;top:170px;width:1200px;height:523px;background:
  radial-gradient(ellipse 180px 260px at 500px 300px,rgba(214,178,150,.7),transparent 70%),
  linear-gradient(100deg,#4a3a2e 0%,#7d6651 25%,#a8927a 50%,#6f5d4c 75%,#3e332b 100%)}
.hero-title{left:0;width:1200px;top:357px;text-align:center;font-family:"Roboto Condensed",Arial,sans-serif;font-size:58px;font-weight:400;color:var(--white)}
.hero-sub{left:0;width:1200px;top:438px;text-align:center;font-size:27px;color:var(--white)}
.hero-arrow{top:414px;width:24px;height:24px;border-radius:50%;background:rgba(0,0,0,.45)}
/* welcome */
.section-title{left:0;width:1200px;text-align:center;font-weight:400;color:var(--ink)}
.welcome-text{left:140px;width:920px;top:843px;text-align:center;font-size:13.5px;line-height:23px;color:var(--muted)}
.feature-back{left:101px;top:971px;width:268px;height:268px;background:#e4e4e4;box-shadow:0 4px 18px rgba(0,0,0,.15)}
.feature-photo{left:120px;top:991px;width:267px;height:271px;background:linear-gradient(160deg,#d9a54a 0%,#c9b37a 45%,#6f8d4c 100%)}
.feature-icon{width:84px;height:84px;border-radius:50%;background:var(--navy);border:4px solid var(--white);box-shadow:0 0 0 2px var(--navy);display:flex;align-items:center;justify-content:center}
.feature h3{font-size:17px;font-weight:400;color:var(--ink);margin-bottom:4px}
.feature p{font-size:12.5px;line-height:18px;color:#8a8a8a;width:230px}
.feature a{font-size:12.5px;color:var(--navy);text-decoration:none;font-weight:600;display:block;margin-top:4px}
/* rent */
.rent-band{left:0;top:1376px;width:1200px;height:269px;background:linear-gradient(90deg,#2c2a27,#5a4c3e 40%,#3a3632 70%,#2b2926)}
.rent-card{left:151px;top:1467px;width:898px;height:327px;background:var(--white);box-shadow:0 6px 24px rgba(0,0,0,.2)}
.rent-photo{left:648px;top:1467px;width:401px;height:327px;background:linear-gradient(150deg,#2f3d55 0%,#6d7c8f 45%,#a8b9c7 70%,#c78c4f 100%)}
.play{left:818px;top:1602px;width:60px;height:60px}
.rent-title{left:193px;top:1515px;font-size:23px;font-weight:400;color:var(--ink)}
.rent-sub{left:193px;top:1545px;font-size:17px;color:var(--navy)}
.rent-text{left:193px;top:1576px;width:410px;font-size:13px;line-height:22px;color:#444}
.btn{left:193px;top:1723px;width:111px;height:34px;border-radius:17px;background:var(--navy);color:var(--white);font-size:13px;line-height:34px;text-align:center}
/* blog */
.blog-card{top:1999px;width:313px;height:288px;background:var(--white);box-shadow:0 2px 10px rgba(0,0,0,.18)}
.blog-img{position:absolute;left:0;top:0;width:313px;height:166px}
.blog-date{position:absolute;left:0;top:142px;background:var(--navy);color:var(--white);font-size:12px;padding:3px 10px}
.blog-card h3{position:absolute;top:182px;width:100%;text-align:center;font-size:18px;font-weight:400}
.blog-card p{position:absolute;top:214px;left:20px;right:20px;text-align:center;font-size:12.5px;line-height:19px;color:#666}
.blog-card a{position:absolute;top:258px;width:100%;text-align:center;font-size:12.5px;color:var(--navy);text-decoration:none}
/* partners */
.partner{top:2450px;width:170px;height:100px;background:#f2f2f2;border:1px solid #e0e0e0;border-radius:4px;display:flex;align-items:center;justify-content:center}
.partner span{width:96px;height:18px;background:#c9c9c9;border-radius:3px}
/* footer */
.footer{left:0;top:2597px;width:1200px;height:306px;background:var(--footer);color:var(--white)}
.footer h4{position:absolute;font-size:15px;font-weight:400;letter-spacing:.3px}
.footer-text{position:absolute;font-size:12.5px;line-height:23px}
.footer-brand{left:91px;top:142px;font-size:14px;font-weight:700;position:absolute}
.footer-brand i{display:inline-block;width:12px;height:12px;background:var(--white);margin-right:8px}
.email{position:absolute;left:654px;top:139px;width:146px;height:30px;background:var(--white);color:#888;font-size:12px;line-height:30px;padding-left:8px}
.submit{position:absolute;left:800px;top:139px;width:54px;height:30px;background:var(--navy);font-size:12px;line-height:30px;text-align:center}
.f-social{position:absolute;left:942px;top:101px;display:flex;gap:12px}
.f-social span{width:24px;height:24px;border-radius:3px;background:var(--white)}
.divider{position:absolute;left:81px;top:218px;width:1022px;height:1px;background:#555}
.copyright{position:absolute;left:0;width:1200px;top:245px;text-align:center;font-size:12.5px}
</style>
</head>
<body>
<header>
  <div class="abs phone">
    <svg width="18" height="18" viewBox="0 0 24 24"><rect width="24" height="24" rx="4" fill="#3a3995"/><path d="M8 5l3 3-2 2c1 2 3 4 5 5l2-2 3 3-2 3C11 19 5 13 5 7z" fill="#fff"/></svg>
    0161 480 2270
  </div>
  <div class="abs brand"><span class="brand-mark"></span>HARBOURLINE LENDING GROUP</div>
  <div class="abs social"><span></span><span></span><span></span><span></span></div>
  <nav class="abs nav">
    <a class="active" style="left:91px;width:124px">HOME</a>
    <a style="left:268px;width:110px">ABOUT</a>
    <a style="left:437px;width:240px">TYPES OF MORTGAGES</a>
    <a style="left:742px;width:150px">RENT TO OWN</a>
    <a style="left:969px;width:145px">CONTACT US</a>
  </nav>
</header>

<section>
  <div class="abs hero" role="img" aria-label="Photograph: hand holding house keys with a house-shaped key ring over a desk of house plans and tools"></div>
  <h1 class="abs hero-title">HARBOURLINE LENDING GROUP</h1>
  <p class="abs hero-sub">Porro quisquam est qui dolorem ipsum</p>
  <div class="abs hero-arrow" style="left:71px"><svg width="24" height="24"><path d="M14 7l-5 5 5 5" stroke="#fff" stroke-width="2" fill="none"/></svg></div>
  <div class="abs hero-arrow" style="left:1105px"><svg width="24" height="24"><path d="M10 7l5 5-5 5" stroke="#fff" stroke-width="2" fill="none"/></svg></div>
</section>

<section>
  <h2 class="abs section-title" style="top:791px;font-size:31px">WELCOME TO HARBOURLINE LENDING GROUP</h2>
  <p class="abs welcome-text">Harbourline Lending Group is a private lender of 1 st ,2 nd , construction and bridge mortgages in Simcoe County area. HLG offers a wide array of financing options to provide assistance to those of you that do not meet the bank's criteria.The reasons could range from bruised credit to inability to provide the banks with the required documentation to meet income qualification guidelines</p>
  <div class="abs feature-back"></div>
  <div class="abs feature-photo" role="img" aria-label="Photograph: hand passing a money bag to an open hand holding a small family house in warm sunlight"></div>

  <div class="abs feature-icon" style="left:432px;top:1003px"><svg width="34" height="30" viewBox="0 0 34 30"><rect x="2" y="2" width="30" height="19" rx="2" fill="none" stroke="#fff" stroke-width="3"/><rect x="12" y="24" width="10" height="3" fill="#fff"/></svg></div>
  <div class="abs feature" style="left:534px;top:1004px"><h3>Down payment</h3><p>We require a minimum down pay-ment of $10,000 or 3.5% to 4% of</p><a>View More »</a></div>

  <div class="abs feature-icon" style="left:780px;top:1003px"><svg width="34" height="26" viewBox="0 0 34 26"><rect x="2" y="3" width="30" height="20" rx="2" fill="none" stroke="#fff" stroke-width="3"/><circle cx="17" cy="13" r="5" fill="#fff"/></svg></div>
  <div class="abs feature" style="left:882px;top:1004px"><h3>Household Income</h3><p>Steady, provable household income that can support the price</p><a>View More »</a></div>

  <div class="abs feature-icon" style="left:432px;top:1140px"><svg width="34" height="26" viewBox="0 0 34 26"><rect x="2" y="2" width="30" height="22" rx="2" fill="none" stroke="#fff" stroke-width="3"/><rect x="2" y="8" width="30" height="4" fill="#fff"/><rect x="7" y="16" width="8" height="3" fill="#fff"/></svg></div>
  <div class="abs feature" style="left:530px;top:1141px"><h3>Credit Report</h3><p>Although your credit won't neces-sarily disqualify you from our</p><a>View More »</a></div>

  <div class="abs feature-icon" style="left:780px;top:1140px"><svg width="32" height="30" viewBox="0 0 32 30"><path d="M16 2L2 15h4v13h8v-8h4v8h8V15h4z" fill="#fff"/></svg></div>
  <div class="abs feature" style="left:880px;top:1141px"><h3>Selecting a House</h3><p>May not seem like a strong deter-mining factor overall for qualifying</p><a>View More »</a></div>
</section>

<section>
  <div class="abs rent-band" role="img" aria-label="Photograph: stacks of coins on a table in warm low light"></div>
  <div class="abs rent-card"></div>
  <div class="abs rent-photo" role="img" aria-label="Photograph: business handshake over a desk with a detached family house, keys and signed papers"></div>
  <svg class="abs play" viewBox="0 0 60 60"><circle cx="30" cy="30" r="28" fill="rgba(0,0,0,.55)"/><path d="M24 18l18 12-18 12z" fill="#fff"/></svg>
  <h2 class="abs rent-title">RENT TO OWN A HOME</h2>
  <p class="abs rent-sub">We Can Put You in Your Own Home Today</p>
  <p class="abs rent-text">We know life sometimes delivers challenges and it can be hard to get back on track once you have dealt with challenges. Maybe you have been through a divorce, bankruptcy, consumer proposal, loss of job, work place injury, new to the country,self-employed or some credit related challenges that have you behind the eight ball? Are these challenges making</p>
  <div class="abs btn">READ MORE</div>
</section>

<section>
  <h2 class="abs section-title" style="top:1923px;font-size:32px">LATEST BLOG</h2>
  <article class="abs blog-card" style="left:97px">
    <div class="blog-img" role="img" aria-label="Photograph: couple reviewing a home purchase with an adviser at a table" style="background:linear-gradient(135deg,#8a7a6a,#c9b9a3 50%,#5c6d7f)"></div>
    <span class="blog-date">JULY 2017</span>
    <h3>Ipsum quia dolor</h3>
    <p>It has survived not only five centuries, but also the leap into electronic typesetting,</p>
    <a>Read More »</a>
  </article>
  <article class="abs blog-card" style="left:435px">
    <div class="blog-img" role="img" aria-label="Photograph: small family house beside stacked coins and a calculator" style="background:linear-gradient(135deg,#e6cf8a,#c89d4a 55%,#8c6a3a)"></div>
    <span class="blog-date">JULY 2017</span>
    <h3>Dolorem ipsum</h3>
    <p>It has survived not only five centuries, but also the leap into electronic typesetting,</p>
    <a>Read More »</a>
  </article>
  <article class="abs blog-card" style="left:774px">
    <div class="blog-img" role="img" aria-label="Photograph: laptop showing a mortgage listings page on a work desk" style="background:linear-gradient(135deg,#b3453d,#d9d2cc 40%,#8e8f96)"></div>
    <span class="blog-date">JULY 2017</span>
    <h3>Porro quisquam</h3>
    <p>It has survived not only five centuries, but also the leap into electronic typesetting,</p>
    <a>Read More »</a>
  </article>
</section>

<section>
  <h2 class="abs section-title" style="top:2375px;font-size:32px">PARTNERS</h2>
  <div class="abs partner" style="left:135px"><span></span></div>
  <div class="abs partner" style="left:319px"><span></span></div>
  <div class="abs partner" style="left:503px"><span></span></div>
  <div class="abs partner" style="left:687px"><span></span></div>
  <div class="abs partner" style="left:871px"><span></span></div>
</section>

<footer class="abs footer">
  <div class="footer-brand"><i></i>HARBOURLINE LENDING GROUP</div>
  <h4 style="left:377px;top:58px">CONTACT US</h4>
  <div class="footer-text" style="left:377px;top:87px;width:190px">Address : 27 Millbrook Lane, Unit 4, ON 40219<br>Phone : 0161 480 2270<br>Email : info@hlgroup.example</div>
  <h4 style="left:652px;top:58px">JOIN OUR MAILING LIST</h4>
  <div class="footer-text" style="left:654px;top:86px;width:210px;line-height:20px">Your about us information would fit here nicely.</div>
  <div class="email">Email address</div>
  <div class="submit">Submit</div>
  <h4 style="left:942px;top:58px">FOLLOW US OUT THERE</h4>
  <div class="f-social"><span></span><span></span><span></span><span></span></div>
  <div class="divider"></div>
  <p class="copyright">Copyright © 2017. All Rights Reserved</p>
</footer>
</body>
</html>
```